Corvin Ridge Campstays

I am Moving from nest Hop and Lodo to host my own website to create direct bookings. I haves booking platform, I just need a website to embed it into. I want a catchy website to attract potential guests to book at my accommodation located near talloway wilderness reserve in Alberta, Canada.

Here is my nest Hop links:
https://www.nesthop-example.ca/stays/2941806735512094417?ref=1&s=52

https://www.nesthop-example.ca/stays/2953718840627715390?ref=1&s=52

https://www.nesthop-example.ca/stays/2867204915583361209?ref=1&s=52

https://www.nesthop-example.ca/stays/2910486632775508143?ref=1&s=52

https://www.nesthop-example.ca/stays/2706359481220617735?ref=1&s=52

```html
<!DOCTYPE html>
<html lang="en">
<head>
<meta charset="utf-8">
<title>Corvin Ridge Campstays</title>
<link href="https://fonts.googleapis.com/css2?family=Montserrat:wght@600;700;800&family=Roboto:wght@400;500;700&display=swap" rel="stylesheet">
<style>
:root{
  --brown:#3a2a1f;
  --brown-deep:#3d2b1f;
  --ink:#222;
  --muted:#666;
  --grey-bg:#f4f4f4;
  --white:#fff;
  --star:#f4a300;
  --pill:#efefef;
}
*{margin:0;padding:0;box-sizing:border-box}
html,body{width:1200px;height:4367px;overflow:hidden}
body{position:relative;font-family:"Roboto",Arial,sans-serif;color:var(--ink);background:var(--white)}
.abs{position:absolute}
.display{font-family:"Montserrat",Arial,sans-serif;font-weight:700;letter-spacing:1px;text-transform:uppercase;white-space:nowrap}
.eyebrow{font-family:"Roboto",Arial,sans-serif;font-size:16px;letter-spacing:1px;text-transform:uppercase;color:#444;text-align:center;width:100%}
.divider{height:3px;width:70px;background:#555}
.btn-dark{background:var(--brown);color:#fff;border-radius:24px;font-weight:700;font-size:14px;display:flex;align-items:center;justify-content:center;text-transform:uppercase}

/* hero */
.hero{left:0;top:0;width:1200px;height:810px;overflow:hidden}
.hero-photo{position:absolute;inset:0;background:linear-gradient(180deg,#aebfcc 0%,#8ea3b3 24%,#5d7282 40%,#3f5a48 56%,#3c4f33 72%,#5b4c3d 100%)}
.logo{left:140px;top:20px;width:180px;text-align:center;color:#2d241e}
.logo-mark{width:46px;height:46px;border-radius:50%;border:3px solid #2d241e;margin:0 auto 8px}
.logo-name{font-family:"Roboto",sans-serif;font-weight:700;font-size:14px;letter-spacing:1px;text-transform:uppercase;line-height:1.2}
.nav{left:446px;top:62px;display:flex;gap:24px;font-size:14px;color:#222}
.book-now{left:935px;top:50px;width:122px;height:42px;background:#fff;border-radius:21px;font-size:14px;font-weight:500;display:flex;align-items:center;justify-content:center}
.hero-kicker{left:0;top:168px;width:1200px;text-align:center;font-size:18px;letter-spacing:1px;color:#2a2a2a;text-transform:uppercase}
.hero-title{left:0;top:206px;width:1200px;text-align:center;font-size:46px;line-height:54px;color:#3a3733}
.hero-btn{left:480px;top:352px;width:238px;height:52px;background:#fff;border-radius:26px;font-weight:700;font-size:17px;letter-spacing:.5px;display:flex;align-items:center;justify-content:center;color:#222}

/* about */
.about-photo{left:145px;top:917px;width:410px;height:410px;border-radius:50%;border:9px solid #6a6a6a;background:linear-gradient(180deg,#2f6fd0 0%,#6ea5e6 45%,#9bb0a5 60%,#8c8f56 80%,#7a7040 100%)}
.about-title{left:622px;top:918px;font-size:34px;line-height:42px;color:var(--brown)}
.about-div{left:622px;top:1013px;background:#555}
.about-sub{left:622px;top:1055px;font-size:18px;font-weight:700;color:#222}
.about-copy{left:622px;top:1094px;width:440px;font-size:13px;line-height:22px;color:var(--muted)}
.about-copy p{margin-bottom:8px}
.about-btn{left:622px;top:1275px;width:150px;height:43px}

/* accommodations */
.accom{left:0;top:1435px;width:1200px;height:670px;background:var(--grey-bg)}
.landscape{left:0;top:2030px;width:1200px;height:410px;background:linear-gradient(180deg,#f4f4f4 0%,#b9c3c9 22%,#6c7b80 42%,#3f4e3f 62%,#6b6a55 85%,#8a7f68 100%)}
.card{width:287px;height:447px;background:#fff;border-radius:10px;box-shadow:0 4px 14px rgba(0,0,0,.18);text-align:center}
.card-photo{position:absolute;left:6px;top:6px;width:275px;height:213px}
.card-title{position:absolute;top:236px;width:100%;font-size:15px;font-weight:500}
.card-loc{position:absolute;top:260px;width:100%;font-size:13px;color:var(--muted)}
.pill{position:absolute;width:115px;height:28px;border-radius:14px;background:var(--pill);border:1px solid #ddd;font-size:13px;display:flex;align-items:center;justify-content:center}
.card-btn{position:absolute;left:77px;top:376px;width:133px;height:40px}
.arrow{width:30px;height:40px}

/* amenities */
.amen{left:0;top:2440px;width:1200px;height:636px;background:var(--brown-deep)}
.feature{width:211px;height:157px;background:#fff;text-align:center}
.feature svg{position:absolute;left:75px;top:28px}
.feature span{position:absolute;left:0;top:108px;width:100%;font-size:15px;font-weight:500;color:#333}

/* testimonials */
.t-card{width:380px;height:217px;background:#fff;border-radius:26px;box-shadow:0 6px 16px rgba(0,0,0,.15)}
.avatar{width:110px;height:110px;border-radius:50%;background:linear-gradient(180deg,#d9dde0,#8a96a0)}
.quote{position:absolute;left:95px;top:28px;font-family:Georgia,serif;font-size:60px;line-height:60px;color:#333}
.t-text{position:absolute;left:95px;top:80px;width:270px;font-size:12px;line-height:21px;color:#888}
.t-name{position:absolute;left:95px;top:148px;font-size:15px;font-weight:500}
.stars{position:absolute;left:95px;top:168px;color:var(--star);font-size:15px;letter-spacing:1px}

/* footer */
.forest{left:0;top:3520px;width:1200px;height:560px;background:linear-gradient(180deg,#fff 0%,#c9cfd3 25%,#4a5258 55%,#0e1114 85%,#000 100%)}
.footer-glow{left:470px;top:3900px;width:240px;height:150px;background:radial-gradient(ellipse at 50% 70%,rgba(200,200,190,.55),rgba(0,0,0,0) 70%)}
.footer{left:0;top:4070px;width:1200px;height:297px;background:#000;color:#fff}
.f-head{font-size:17px;font-weight:700}
.f-item{font-size:13px;display:flex;align-items:center;gap:14px}
.f-link{font-size:13px;line-height:25px}
.email-input{left:706px;top:4135px;width:222px;height:42px;border-radius:21px;background:#fff;color:#888;font-size:12px;padding-left:22px;display:flex;align-items:center}
.submit{left:940px;top:4135px;width:115px;height:42px;border-radius:21px;background:#6b6b6b;color:#fff;font-weight:700;font-size:15px;display:flex;align-items:center;justify-content:center}
.social{width:30px;height:30px;border:1.5px solid #fff;border-radius:50%}
.rule{left:143px;top:4302px;width:914px;height:1px;background:#444}
.copy{left:0;top:4332px;width:1200px;text-align:center;font-size:12px}
</style>
</head>
<body>

<!-- HERO -->
<section class="abs hero">
  <div class="hero-photo" role="img" aria-label="Photo of a white geodesic glamping dome on a wooden deck with red chairs, forest, mountains and a rainbow"></div>
</section>
<div class="abs logo">
  <div class="logo-mark"></div>
  <div class="logo-name">Corvin Ridge<br>Campstays</div>
</div>
<nav class="abs nav"><span>Home</span><span>About Us</span><span>Our Domes</span><span>Amenities</span><span>FAQ</span><span>Contact Us</span></nav>
<div class="abs book-now">Book Now</div>
<div class="abs hero-kicker">Corvin Ridge Campstays</div>
<h1 class="abs hero-title display">Sleep under the<br>stars of Talloway</h1>
<div class="abs hero-btn">BOOK YOUR DOME</div>

<!-- ABOUT -->
<div class="abs about-photo" role="img" aria-label="Photo of a sunny meadow with a fence line, pine trees and distant hills"></div>
<h2 class="abs about-title display">About Corvin Ridge<br>Campstays</h2>
<div class="abs divider about-div"></div>
<div class="abs about-sub">Dome in Talloway County, Canada</div>
<div class="abs about-copy">
  <p>This unique stay is a balance of camping and glamour - hence Glamping! &nbsp;Each unit contains luxurious sleeping quarters and amenities such a coffee machine, fireplace, microwave, and wifi. &nbsp;The scenic stay is heavily influenced by the serene &nbsp;mountain views.</p>
  <p>Outdoor picnic tables, campfires, hammocks are some of the way our guests can relax in nature.</p>
</div>
<div class="abs btn-dark about-btn">Learn More</div>

<!-- ACCOMMODATIONS -->
<section class="abs accom"></section>
<div class="abs landscape" role="img" aria-label="Photo of a wide valley with forest, a small village and mountains"></div>
<div class="abs eyebrow" style="top:1506px">Our Accommodations</div>
<h2 class="abs display" style="left:0;top:1532px;width:1200px;text-align:center;font-size:35px;color:var(--brown)">Five Extraordinary Domes</h2>
<div class="abs divider" style="left:565px;top:1593px"></div>

<svg class="abs arrow" style="left:74px;top:1842px" viewBox="0 0 30 40"><polyline points="20,6 8,20 20,34" fill="none" stroke="#555" stroke-width="4"/></svg>
<svg class="abs arrow" style="left:1098px;top:1842px" viewBox="0 0 30 40"><polyline points="10,6 22,20 10,34" fill="none" stroke="#555" stroke-width="4"/></svg>

<article class="abs card" style="left:145px;top:1638px">
  <div class="card-photo" style="background:linear-gradient(180deg,#c8d0d8,#4d5e46 60%,#8a7a60)" role="img" aria-label="Photo of a dome beside a shed among pine trees"></div>
  <div class="card-title">1 Dome - Corvin Ridge Campstays</div>
  <div class="card-loc">Talloway County, Canada</div>
  <div class="pill" style="left:22px;top:293px">4 guests</div><div class="pill" style="left:150px;top:293px">1 bedroom</div>
  <div class="pill" style="left:22px;top:332px">4 guests</div><div class="pill" style="left:150px;top:332px">1 bedroom</div>
  <div class="btn-dark card-btn">Viewdetails</div>
</article>
<article class="abs card" style="left:457px;top:1655px">
  <div class="card-photo" style="background:linear-gradient(180deg,#d9cfbd,#a48f72 55%,#c5a27a)" role="img" aria-label="Photo of a dome interior with an armchair and a bed"></div>
  <div class="card-title">2 Dome - Corvin Ridge Campstays</div>
  <div class="card-loc">Talloway County, Canada</div>
  <div class="pill" style="left:22px;top:293px">4 guests</div><div class="pill" style="left:150px;top:293px">1 bedroom</div>
  <div class="pill" style="left:22px;top:332px">4 guests</div><div class="pill" style="left:150px;top:332px">1 bedroom</div>
  <div class="btn-dark card-btn">Viewdetails</div>
</article>
<article class="abs card" style="left:769px;top:1638px">
  <div class="card-photo" style="background:linear-gradient(180deg,#5c90d8,#9fb8d8 45%,#dde6f0)" role="img" aria-label="Photo of a dome in snow under a blue sky"></div>
  <div class="card-title">3 Dome - Corvin Ridge Campstays</div>
  <div class="card-loc">Talloway County, Canada</div>
  <div class="pill" style="left:22px;top:293px">4 guests</div><div class="pill" style="left:150px;top:293px">1 bedroom</div>
  <div class="pill" style="left:22px;top:332px">4 guests</div><div class="pill" style="left:150px;top:332px">1 bedroom</div>
  <div class="btn-dark card-btn">Viewdetails</div>
</article>

<!-- AMENITIES -->
<section class="abs amen"></section>
<div class="abs eyebrow" style="top:2512px;color:#fff">What's Included</div>
<h2 class="abs display" style="left:0;top:2538px;width:1200px;text-align:center;font-size:35px;color:#fff">Luxury Meets the Wild</h2>
<div class="abs divider" style="left:565px;top:2599px;background:#aaa"></div>

<div class="abs feature" style="left:145px;top:2657px">
  <svg width="60" height="60" viewBox="0 0 60 60" fill="none" stroke="#555" stroke-width="2"><path d="M6 24 30 8 54 24v30H6z"/><rect x="16" y="30" width="28" height="24"/><rect x="21" y="38" width="18" height="10" rx="3"/></svg>
  <span>Free parking on premises</span>
</div>
<div class="abs feature" style="left:377px;top:2657px">
  <svg width="60" height="60" viewBox="0 0 60 60" fill="none" stroke="#555" stroke-width="2.5"><path d="M6 24a34 34 0 0 1 48 0"/><path d="M14 32a22 22 0 0 1 32 0"/><path d="M22 40a11 11 0 0 1 16 0"/><circle cx="30" cy="48" r="3"/></svg>
  <span>High-speed WI-FI</span>
</div>
<div class="abs feature" style="left:611px;top:2657px">
  <svg width="60" height="60" viewBox="0 0 60 60" fill="none" stroke="#555" stroke-width="2"><rect x="2" y="10" width="56" height="24" rx="3"/><line x1="8" y1="28" x2="52" y2="28"/><path d="M18 40l-2 8M26 40v8M34 40v8M42 40l2 8"/></svg>
  <span>Air conditioning</span>
</div>
<div class="abs feature" style="left:844px;top:2657px">
  <svg width="60" height="60" viewBox="0 0 60 60" fill="none" stroke="#555" stroke-width="2"><path d="M18 6c-4 4 4 6 0 12M28 6c-4 4 4 6 0 12M38 6c-4 4 4 6 0 12"/><path d="M8 26h44v20a8 8 0 0 1-8 8H16a8 8 0 0 1-8-8z"/><circle cx="22" cy="38" r="3"/><circle cx="38" cy="38" r="3"/></svg>
  <span>Hot water</span>
</div>
<div class="abs feature" style="left:145px;top:2836px">
  <svg width="60" height="60" viewBox="0 0 60 60" fill="none" stroke="#555" stroke-width="2"><rect x="2" y="12" width="56" height="36" rx="3"/><rect x="8" y="18" width="34" height="24"/><circle cx="50" cy="22" r="2"/><circle cx="50" cy="30" r="2"/><path d="M20 24c-2 3 2 5 0 10M26 24c-2 3 2 5 0 10"/></svg>
  <span>Microwave</span>
</div>
<div class="abs feature" style="left:377px;top:2836px">
  <svg width="60" height="60" viewBox="0 0 60 60" fill="none" stroke="#555" stroke-width="2"><rect x="8" y="6" width="44" height="46" rx="3"/><rect x="14" y="12" width="32" height="34"/><circle cx="26" cy="29" r="6"/><line x1="38" y1="22" x2="38" y2="36"/><path d="M14 52v4M46 52v4"/></svg>
  <span>Lockbox</span>
</div>
<div class="abs feature" style="left:611px;top:2836px">
  <svg width="60" height="60" viewBox="0 0 60 60" fill="none" stroke="#555" stroke-width="2"><path d="M30 4c-6 8 6 10 0 20M22 10c-4 6 4 8 0 14M38 10c-4 6 4 8 0 14"/><path d="M8 28h44l-6 12H14z"/><path d="M18 40l-6 14M42 40l6 14M30 40v14"/></svg>
  <span>Fire pit</span>
</div>
<div class="abs feature" style="left:844px;top:2836px">
  <svg width="60" height="60" viewBox="0 0 60 60" fill="none" stroke="#555" stroke-width="2"><rect x="10" y="4" width="40" height="52" rx="3"/><line x1="10" y1="22" x2="50" y2="22"/><rect x="16" y="28" width="10" height="20"/><rect x="30" y="34" width="14" height="14"/><line x1="16" y1="12" x2="16" y2="18"/></svg>
  <span>Mini fridge</span>
</div>

<!-- TESTIMONIALS -->
<div class="abs eyebrow" style="top:3155px">Testimonials</div>
<h2 class="abs display" style="left:0;top:3182px;width:1200px;text-align:center;font-size:35px;color:var(--brown)">What Our Client Says</h2>
<div class="abs divider" style="left:565px;top:3243px"></div>

<svg class="abs arrow" style="left:74px;top:3392px" viewBox="0 0 30 40"><polyline points="20,6 8,20 20,34" fill="none" stroke="#555" stroke-width="4"/></svg>
<svg class="abs arrow" style="left:1098px;top:3392px" viewBox="0 0 30 40"><polyline points="10,6 22,20 10,34" fill="none" stroke="#555" stroke-width="4"/></svg>

<article class="abs t-card" style="left:198px;top:3303px">
  <div class="quote">&ldquo;</div>
  <p class="t-text">Sed ut perspiciatis unde omnis iste natus error sit voluptatem accusantium doloremque laudantium, totam rem aperiam,</p>
  <div class="t-name">Dario Mendel</div>
  <div class="stars">★★★★★</div>
</article>
<div class="abs avatar" style="left:148px;top:3357px" role="img" aria-label="Guest portrait"></div>
<article class="abs t-card" style="left:675px;top:3303px">
  <div class="quote">&ldquo;</div>
  <p class="t-text">Sed ut perspiciatis unde omnis iste natus error sit voluptatem accusantium doloremque laudantium, totam rem aperiam,</p>
  <div class="t-name">Priya Aldous</div>
  <div class="stars">★★★★★</div>
</article>
<div class="abs avatar" style="left:625px;top:3357px" role="img" aria-label="Guest portrait"></div>

<!-- FOOTER -->
<div class="abs forest" role="img" aria-label="Photo of a pine forest silhouette fading into night"></div>
<div class="abs footer-glow" role="img" aria-label="Photo of a lit glamping dome at night"></div>
<footer class="abs footer"></footer>

<div class="abs f-head" style="left:143px;top:4090px;color:#fff">Contact Us</div>
<div class="abs f-item" style="left:145px;top:4132px;color:#fff">
  <svg width="12" height="14" viewBox="0 0 12 14"><path d="M6 0a5 5 0 0 1 5 5c0 4-5 9-5 9S1 9 1 5a5 5 0 0 1 5-5z" fill="#c9a070"/><circle cx="6" cy="5" r="2" fill="#000"/></svg>Talloway County, Alberta, Canada</div>
<div class="abs f-item" style="left:145px;top:4169px;color:#fff">
  <svg width="14" height="11" viewBox="0 0 14 11"><rect width="14" height="11" fill="#c9a070"/><polyline points="0,0 7,6 14,0" fill="none" stroke="#000" stroke-width="1.2"/></svg>info@corvinridgecampstays.com</div>
<div class="abs f-item" style="left:145px;top:4205px;color:#fff">
  <svg width="13" height="13" viewBox="0 0 13 13"><path d="M2 0l3 3-1.5 2a8 8 0 0 0 4.5 4.5L10 8l3 3-2 2C5 13 0 8 0 2z" fill="#c9a070"/></svg>+1 587-555-0148</div>
<div class="abs f-item" style="left:145px;top:4239px;color:#fff">
  <svg width="14" height="13" viewBox="0 0 14 13"><rect x="0" y="3" width="14" height="10" fill="#c9a070"/><rect x="3" y="0" width="8" height="5" fill="#c9a070" stroke="#000"/><rect x="3" y="7" width="8" height="3" fill="#000"/></svg>587 555 0193</div>

<div class="abs f-head" style="left:440px;top:4090px;color:#fff">Links</div>
<div class="abs f-link" style="left:441px;top:4128px;color:#fff">Home<br>About Us<br>Our Domes<br>Amenities<br>FAQ</div>
<div class="abs f-link" style="left:546px;top:4128px;color:#fff">Terms &amp; Condition<br>Privacy Policy<br>Support<br>Site Map<br>Contact Us</div>

<div class="abs f-head" style="left:703px;top:4090px;color:#fff">Subscribe for Updates</div>
<div class="abs email-input">Email Address</div>
<div class="abs submit">SUBMIT</div>
<div class="abs f-item" style="left:704px;top:4200px;color:#fff;gap:8px;font-size:12px">
  <svg width="12" height="12" viewBox="0 0 12 12"><rect x="1" y="1" width="10" height="10" fill="none" stroke="#fff"/><polyline points="3,6 5,8 9,3" fill="none" stroke="#fff" stroke-width="1.5"/></svg>Yes, Please Contact me.</div>
<div class="abs social" style="left:703px;top:4235px"></div>
<div class="abs social" style="left:742px;top:4235px"></div>
<div class="abs social" style="left:782px;top:4235px"></div>

<div class="abs rule"></div>
<div class="abs copy" style="color:#fff">© 2026 &nbsp;Corvin Ridge Campstays &nbsp;| &nbsp;All Rights Reserved</div>

</body>
</html>
```